Web Site for Strategy and Technology Consulting Company

We are looking for a website design that engages potential customers to understand our services and contact us. In this contest, we are looking for a homepage design, but the winning designer will be favored for the design of some of the more complicated interior pages of the site. An additional contest (or contests) for these pages will be added soon.

PLATROM AND RESPONSIVE DESIGN
The site will be implemented in WordPress using the Elementor page builder.
We are looking for a design that will look good on phones are well as laptop browsers.

UPLOADED FILES INCLUDE:
1a A wireframe of the homepage we are looking for. The Uploaded PDF also includes a draft of the text proposed for the homepage. Designers are free to go beyond the wireframe, but all elements of the wireframe should be included.
1b A Word document with the draft text of the homepage.
2a-d The Norvalith logo. Two versions are included – a dark version which works well against a light background, and a light version which works well against a dark background.
3 The Norvalith color palette with HEX and RGB values. Designers are not limited to this palette, but colors should be complementary.
4 A draft of the homepage menu
5 Service sheets with information on the services we provide

MORE ABOUT NORVALITH
Norvalith is a consulting company focused on transforming businesses through software. Our tagline, “Transformation Delivered,” recognizes the gap business often have between business transformation and the software they end up with. By listening to our customers and understanding their vision and where they are, we help get our customers where they want to go.

We increase our capability by working with many consultants and partners, allowing us to provide our customers with the best people and the software that best suits them.

Industry/Entity Type

Consulting

Number of Pages Required

1 page

Font styles to use
Sans Serif

Requirements
Must have
• the content represented on the wireframe uploaded
Nice to have
• interactive features, such as roll-over icons that reveal additional information

```html
<!DOCTYPE html>
<html lang="en">
<head>
<meta charset="utf-8">
<title>Norvalith – Transformation Delivered</title>
<link href="https://fonts.googleapis.com/css2?family=Montserrat:wght@500;600;700;800&family=Open+Sans:wght@400;600;700&display=swap" rel="stylesheet">
<style>
:root{
  --navy:#0a2f5c;
  --navy-deep:#061d3d;
  --blue:#1a5fb4;
  --blue-bright:#2f80d8;
  --yellow:#f5c518;
  --ink:#1b1f2a;
  --text:#4a5160;
  --muted:#7b8291;
  --line:#e3e7ee;
  --soft:#eef2f7;
  --black:#0c0d10;
  --white:#ffffff;
  --star:#f2a91c;
}
*{box-sizing:border-box;margin:0;padding:0}
html,body{width:1200px;height:3248px;overflow:hidden}
body{font-family:"Open Sans",Arial,sans-serif;color:var(--text);background:var(--white);position:relative}
h1,h2,h3,h4,.brand,.btn,.nav a{font-family:"Montserrat",Arial,sans-serif}

/* header */
.site-header{position:absolute;top:0;left:0;width:1200px;height:90px;background:var(--white);display:flex;align-items:center;padding:0 40px;box-shadow:0 2px 8px rgba(0,0,0,.06)}
.brand{display:flex;align-items:center;gap:10px;font-size:30px;font-weight:700;color:var(--navy);letter-spacing:.2px}
.brand-dot{width:14px;height:14px;background:var(--blue)}
.nav{margin-left:auto;display:flex;align-items:center;gap:40px}
.nav a{font-size:15px;font-weight:600;color:var(--ink);text-decoration:none;position:relative}
.nav a.active{color:var(--blue)}
.nav a.active::after{content:"";position:absolute;left:0;right:0;bottom:-8px;height:2px;background:var(--blue)}
.btn{display:inline-flex;align-items:center;gap:10px;font-weight:700;font-size:13px;letter-spacing:.6px;text-transform:uppercase;text-decoration:none;border-radius:3px}
.btn-blue{background:var(--blue);color:var(--white);padding:14px 22px}
.btn-navy{background:var(--navy);color:var(--white);padding:13px 22px}
.btn-yellow{background:var(--yellow);color:var(--ink);padding:14px 26px}
.btn .arrow{width:18px;height:18px;border-radius:50%;background:var(--white);display:inline-flex;align-items:center;justify-content:center}

/* hero */
.hero{position:absolute;top:90px;left:0;width:1200px;height:690px;overflow:hidden}
.hero-art{position:absolute;inset:0;background:radial-gradient(circle at 78% 55%,#1f6fc8 0%,#0f4a93 30%,#082c5e 65%,#051b3b 100%)}
.hero-inner{position:absolute;left:60px;top:70px;width:620px;color:var(--white)}
.hero h1{font-size:50px;font-weight:700;color:var(--yellow);margin-bottom:24px}
.hero-lead{font-size:17px;font-weight:700;line-height:1.65;margin-bottom:30px}
.hero-list{list-style:none;font-size:14.5px;line-height:2}
.hero-list li{display:flex;gap:12px;align-items:center}
.hero-list li::before{content:"";width:7px;height:7px;border-radius:50%;background:var(--yellow);flex:none}
.hero-tag{margin-top:28px;font-size:14.5px}
.hero-dots{position:absolute;left:60px;bottom:44px;display:flex;gap:10px}
.hero-dots span{width:9px;height:9px;border-radius:50%;background:rgba(255,255,255,.4)}
.hero-dots span.on{background:var(--white)}

/* section heading */
.section-title{text-align:center;font-size:38px;font-weight:800;color:var(--ink);text-transform:uppercase;letter-spacing:.3px}
.title-bar{width:90px;height:4px;background:var(--blue);margin:14px auto 0}

/* transformation */
.transform{position:absolute;top:780px;left:0;width:1200px;height:700px;padding-top:70px;background:var(--white)}
.transform-intro{width:900px;margin:28px auto 0;text-align:center;font-size:15px;line-height:1.7}
.diff-title{text-align:center;font-size:22px;font-weight:700;color:var(--ink);text-transform:uppercase;margin-top:26px}
.diff-cta{text-align:center;margin-top:20px}
.cards{display:flex;justify-content:center;gap:24px;margin-top:34px}
.card{width:184px;text-align:center}
.card h4{font-size:15px;font-weight:700;color:var(--ink);height:48px;display:flex;align-items:flex-end;justify-content:center;line-height:1.3;margin-bottom:14px}
.card-box{height:168px;border:1px solid var(--line);border-radius:8px;box-shadow:0 6px 18px rgba(10,47,92,.1);padding:26px 16px 0;display:flex;flex-direction:column;align-items:center;gap:18px}
.card-box p{font-size:12.5px;line-height:1.5;color:var(--text)}
.transform-foot{text-align:center;font-size:22px;color:var(--ink);margin-top:50px}

/* resources */
.resources{position:absolute;top:1480px;left:0;width:1200px;height:400px;overflow:hidden}
.resources-art{position:absolute;inset:0;background:linear-gradient(100deg,#0a3a78 0%,#0f4d97 50%,#0a3a78 100%)}
.res-left{position:absolute;left:110px;top:52px;width:440px;color:var(--white)}
.res-left h2{font-size:32px;font-weight:800;text-transform:uppercase}
.res-bar{width:70px;height:4px;background:var(--yellow);margin:10px 0 22px}
.res-left h3{font-size:22px;font-weight:600;color:var(--yellow);margin-bottom:14px}
.res-left p{font-size:14.5px;line-height:1.7}
.res-right{position:absolute;left:640px;top:120px;width:470px;color:var(--white);font-size:14.5px;line-height:1.7}
.res-right ul{list-style:none;margin-bottom:20px}
.res-right li{display:flex;gap:12px;margin-bottom:8px}
.res-right li::before{content:"";width:7px;height:7px;border-radius:50%;background:var(--yellow);flex:none;margin-top:9px}
.res-cta{position:absolute;left:520px;top:300px}

/* testimonials */
.testimonials{position:absolute;top:1880px;left:0;width:1200px;height:560px;background:var(--soft);overflow:hidden;padding-top:62px}
.t-track{position:absolute;top:190px;left:0;width:1200px;height:270px}
.t-card{position:absolute;top:0;width:262px;height:252px;background:var(--white);border-radius:8px;box-shadow:0 6px 18px rgba(10,47,92,.1);padding:22px 20px}
.t-head{display:flex;align-items:center;gap:12px;margin-bottom:14px}
.avatar{width:54px;height:54px;border-radius:50%;background:linear-gradient(135deg,#c9b39c,#8b7560);flex:none}
.t-name{font-family:"Montserrat",Arial,sans-serif;font-weight:700;color:var(--blue);font-size:15px}
.t-role{font-size:12px;color:var(--muted)}
.t-text{font-size:13px;line-height:1.6;color:var(--text)}
.stars{display:flex;gap:4px;margin-top:14px}
.t-dots{position:absolute;top:480px;left:0;width:1200px;display:flex;justify-content:center;gap:8px}
.t-dots span{width:8px;height:8px;border-radius:50%;background:#b8c2d1}
.t-dots span.on{background:var(--blue)}

/* technologies */
.tech{position:absolute;top:2440px;left:0;width:1200px;height:400px;padding-top:78px}
.tech-row{position:absolute;top:220px;left:0;width:1200px;height:80px;display:flex;align-items:center}
.tech-arrow{position:absolute;top:20px;width:36px;height:36px;border-radius:50%;border:1px solid var(--line);display:flex;align-items:center;justify-content:center;background:var(--white)}
.tech-logo{position:absolute;top:0;height:80px;display:flex;align-items:center;justify-content:center;font-family:"Montserrat",Arial,sans-serif;font-weight:600;color:#3a4150}
.tech-logo.sm{font-size:16px;border:1px solid var(--line);border-radius:6px;box-shadow:0 4px 12px rgba(0,0,0,.06);height:70px;top:5px}

/* footer */
.site-footer{position:absolute;top:2840px;left:0;width:1200px;height:408px;background:var(--black);color:#cfd3da}
.f-brand{position:absolute;left:60px;top:80px}
.f-brand .brand{color:var(--white)}
.socials{display:flex;gap:10px;margin-top:22px}
.socials span{width:30px;height:30px;border-radius:50%;background:#3a3d44}
.f-col{position:absolute;top:62px}
.f-col h4{font-size:16px;font-weight:700;color:var(--white);text-transform:uppercase;padding-left:12px;border-left:4px solid var(--yellow);margin-bottom:22px}
.f-col ul{list-style:none;font-size:12.5px;line-height:2.1;text-transform:uppercase;color:#c5c9d1}
.contact-item{display:flex;gap:12px;margin-bottom:16px;font-size:12.5px;line-height:1.5}
.contact-item .ic{width:28px;height:28px;border-radius:4px;background:#2a2d33;flex:none;display:flex;align-items:center;justify-content:center}
.contact-item small{display:block;color:#8f95a0;font-size:11px}
.f-bottom{position:absolute;left:0;bottom:0;width:1200px;height:66px;border-top:1px solid #26292f;display:flex;align-items:center;justify-content:center;font-size:13px;color:#9aa0aa}
.chat{position:absolute;right:22px;bottom:36px;width:44px;height:44px;border-radius:50%;background:var(--yellow);display:flex;align-items:center;justify-content:center}
</style>
</head>
<body>

<header class="site-header">
  <div class="brand"><span class="brand-dot"></span>Norvalith</div>
  <nav class="nav">
    <a href="#" class="active">Home</a>
    <a href="#">About Us</a>
    <a href="#">Services</a>
    <a href="#">Insights</a>
    <a href="#">Join Us</a>
    <a href="#" class="btn btn-blue">Contact Us <span class="arrow"><svg width="10" height="10" viewBox="0 0 10 10"><path d="M2 5h6M5.5 2.5 8 5 5.5 7.5" stroke="#1a5fb4" stroke-width="1.6" fill="none"/></svg></span></a>
  </nav>
</header>

<section class="hero">
  <div class="hero-art" role="img" aria-label="Deep blue background with glowing digital circuit lines"></div>
  <div class="hero-inner">
    <h1>Transformation Delivered</h1>
    <p class="hero-lead">We do more for our customers than implement software. We listen. We work to understand where they are in their transformation journey and where they want to go. We partner with them to clear the roadblocks that stand in their way, ensuring they reach their destination. At Norvalith, we:</p>
    <ul class="hero-list">
      <li>Focus on business value, with an emphasis on delivering value quickly.</li>
      <li>Meet our customers where they are without backing them up to the beginning of their journey.</li>
      <li>Provide a wide range of services, from strategy to product support.</li>
      <li>Commit to our customer's long-term success.</li>
    </ul>
    <p class="hero-tag">Norvalith is business transformation, delivered.</p>
  </div>
  <div class="hero-dots"><span class="on"></span><span></span><span></span><span></span></div>
</section>

<section class="transform">
  <h2 class="section-title">Transformation Supported by Technology</h2>
  <div class="title-bar"></div>
  <p class="transform-intro">During our early years, Norvalith focused only on business transformation. We came to realize that successful transformation often depended on quality software implementations, and often more than one. Now we focus on five things, the five things most businesses need to reach their goals.</p>
  <h3 class="diff-title">Differentiators Around Our Services</h3>
  <div class="diff-cta"><a href="#" class="btn btn-navy">How We Work <span class="arrow"><svg width="10" height="10" viewBox="0 0 10 10"><path d="M2 5h6M5.5 2.5 8 5 5.5 7.5" stroke="#0a2f5c" stroke-width="1.6" fill="none"/></svg></span></a></div>
  <div class="cards">
    <div class="card"><h4>Business<br>Transformation</h4>
      <div class="card-box"><svg width="54" height="54" viewBox="0 0 54 54" fill="none" stroke="#1a5fb4" stroke-width="2"><circle cx="27" cy="27" r="20"/><circle cx="27" cy="27" r="12"/><circle cx="27" cy="27" r="4" fill="#1a5fb4"/><path d="M27 27 44 10M40 10h4v4"/></svg><p>Define and execute your strategy</p></div></div>
    <div class="card"><h4>ERP<br>Implementations</h4>
      <div class="card-box"><svg width="54" height="54" viewBox="0 0 54 54" fill="none" stroke="#1a5fb4" stroke-width="2"><rect x="8" y="10" width="38" height="28" rx="2"/><path d="M20 46h14M27 38v8M15 30l8-8 6 5 10-10"/></svg><p>Assess, upgrade &amp; implement ERP solutions to meet your needs</p></div></div>
    <div class="card"><h4>CRM<br>Implementations</h4>
      <div class="card-box"><svg width="54" height="54" viewBox="0 0 54 54" fill="none" stroke="#1a5fb4" stroke-width="2"><circle cx="27" cy="18" r="7"/><path d="M14 44c0-8 6-13 13-13s13 5 13 13"/><circle cx="10" cy="24" r="4"/><circle cx="44" cy="24" r="4"/></svg><p>Take your relationships to the next level</p></div></div>
    <div class="card"><h4>BI and<br>Data</h4>
      <div class="card-box"><svg width="54" height="54" viewBox="0 0 54 54" fill="none" stroke="#1a5fb4" stroke-width="2"><path d="M8 46h38"/><rect x="12" y="28" width="7" height="18"/><rect x="24" y="18" width="7" height="28"/><rect x="36" y="10" width="7" height="36"/></svg><p>Discover, connect &amp; trust your data</p></div></div>
    <div class="card"><h4>Building the Right<br>Team of People</h4>
      <div class="card-box"><svg width="54" height="54" viewBox="0 0 54 54" fill="none" stroke="#1a5fb4" stroke-width="2"><circle cx="18" cy="20" r="6"/><circle cx="36" cy="20" r="6"/><path d="M6 42c0-7 5-11 12-11s12 4 12 11M24 42c0-7 5-11 12-11s12 4 12 11"/></svg><p>Hire resources for your transformation journey</p></div></div>
  </div>
  <p class="transform-foot">Find out how Norvalith can help you put all the pieces together and get them done.</p>
</section>

<section class="resources">
  <div class="resources-art" role="img" aria-label="Blue background with faint digital network lines"></div>
  <div class="res-left">
    <h2>Resources</h2>
    <div class="res-bar"></div>
    <h3>It's the People</h3>
    <p>The world has changed in the past twenty years. The people you need might not all work for one company. Our clients want the best resources, available quickly. That's why, in addition to our team of experts, we partner with:</p>
  </div>
  <div class="res-right">
    <ul>
      <li>A large network of expert consultants who are the best at what they do.</li>
      <li>Service providers all over the world to provide the resources and value that are right for you, available 24x7.</li>
    </ul>
    <p>People are invariably at the center of our customer's success. Find out how we can add our experts to yours.</p>
  </div>
  <div class="res-cta"><a href="#" class="btn btn-yellow">Our Team <svg width="14" height="14" viewBox="0 0 14 14"><path d="M2 7h9M8 3.5 11.5 7 8 10.5" stroke="#1b1f2a" stroke-width="1.8" fill="none"/></svg></a></div>
</section>

<section class="testimonials">
  <h2 class="section-title">Testimonials</h2>
  <div class="title-bar"></div>
  <div class="t-track">
    <div class="t-card" style="left:-214px">
      <div class="t-head"><div class="avatar" role="img" aria-label="Client portrait"></div><div><div class="t-name">Daniel Harlow</div><div class="t-role">Director, Brightline</div></div></div>
      <p class="t-text">Their team listened first and built a plan that fit how we work. The rollout was smooth and our people adopted it fast.</p>
    </div>
    <div class="t-card" style="left:76px">
      <div class="t-head"><div class="avatar" role="img" aria-label="Client portrait"></div><div><div class="t-name">Daniel Harlow</div><div class="t-role">Director, Brightline</div></div></div>
      <p class="t-text">Their team listened first and built a plan that fit how we work. The rollout was smooth and our people adopted it fast.</p>
      <div class="stars"><svg width="100" height="16" viewBox="0 0 100 16"><g fill="#f2a91c"><path id="s" d="M8 1l2.1 4.5 4.9.6-3.6 3.4.9 4.9L8 12l-4.3 2.4.9-4.9L1 6.1l4.9-.6z"/><use href="#s" x="20"/><use href="#s" x="40"/><use href="#s" x="60"/><use href="#s" x="80"/></g></svg></div>
    </div>
    <div class="t-card" style="left:366px">
      <div class="t-head"><div class="avatar" role="img" aria-label="Client portrait"></div><div><div class="t-name">Daniel Harlow</div><div class="t-role">Director, Brightline</div></div></div>
      <p class="t-text">We finally have one view of our data. Reports that took days now take minutes, and decisions are made with confidence.</p>
      <div class="stars"><svg width="100" height="16" viewBox="0 0 100 16"><g fill="#f2a91c"><use href="#s"/><use href="#s" x="20"/><use href="#s" x="40"/><use href="#s" x="60"/><use href="#s" x="80"/></g></svg></div>
    </div>
    <div class="t-card" style="left:656px">
      <div class="t-head"><div class="avatar" role="img" aria-label="Client portrait"></div><div><div class="t-name">Daniel Harlow</div><div class="t-role">Director, Brightline</div></div></div>
      <p class="t-text">They met us where we were and kept the focus on value. Every phase delivered something useful to our business teams.</p>
      <div class="stars"><svg width="100" height="16" viewBox="0 0 100 16"><g fill="#f2a91c"><use href="#s"/><use href="#s" x="20"/><use href="#s" x="40"/><use href="#s" x="60"/><use href="#s" x="80"/></g></svg></div>
    </div>
    <div class="t-card" style="left:946px">
      <div class="t-head"><div class="avatar" role="img" aria-label="Client portrait"></div><div><div class="t-name">Daniel Harlow</div><div class="t-role">Director, Brightline</div></div></div>
      <p class="t-text">The consultants they brought in were experts in our industry. Our new CRM is now at the heart of how we sell.</p>
      <div class="stars"><svg width="100" height="16" viewBox="0 0 100 16"><g fill="#f2a91c"><use href="#s"/><use href="#s" x="20"/><use href="#s" x="40"/><use href="#s" x="60"/><use href="#s" x="80"/></g></svg></div>
    </div>
  </div>
  <div class="t-dots"><span></span><span class="on"></span><span></span><span></span></div>
</section>

<section class="tech">
  <h2 class="section-title">Technologies</h2>
  <div class="title-bar"></div>
  <div class="tech-row">
    <div class="tech-arrow" style="left:60px"><svg width="12" height="12" viewBox="0 0 12 12"><path d="M8 2 4 6l4 4" stroke="#4a5160" stroke-width="1.8" fill="none"/></svg></div>
    <div class="tech-logo" style="left:130px;width:220px;font-size:22px">Veridia Suite 365</div>
    <div class="tech-logo sm" style="left:400px;width:160px">Korvane</div>
    <div class="tech-logo" style="left:620px;width:230px;font-size:20px">Korvane CloudSuite</div>
    <div class="tech-logo" style="left:900px;width:180px;font-size:26px">Shiftly</div>
    <div class="tech-arrow" style="left:1104px"><svg width="12" height="12" viewBox="0 0 12 12"><path d="M4 2l4 4-4 4" stroke="#4a5160" stroke-width="1.8" fill="none"/></svg></div>
  </div>
</section>

<footer class="site-footer">
  <div class="f-brand">
    <div class="brand"><span class="brand-dot"></span>Norvalith</div>
    <div class="socials"><span></span><span></span><span></span><span></span></div>
  </div>
  <div class="f-col" style="left:400px">
    <h4>Quick Links</h4>
    <ul><li>Home</li><li>About Us</li><li>Services</li><li>Insights</li><li>Join Us</li><li>Contact Us</li></ul>
  </div>
  <div class="f-col" style="left:630px">
    <h4>Links</h4>
    <ul><li>Copyright</li><li>Legal</li><li>Privacy</li><li>Accessibility</li><li>Sitemap</li></ul>
  </div>
  <div class="f-col" style="left:830px;width:300px">
    <h4>Contact Us</h4>
    <div class="contact-item"><span class="ic"><svg width="14" height="14" viewBox="0 0 14 14"><path d="M7 13s4.5-4.5 4.5-7.5a4.5 4.5 0 0 0-9 0C2.5 8.5 7 13 7 13z" fill="none" stroke="#f5c518" stroke-width="1.4"/><circle cx="7" cy="5.5" r="1.5" fill="#f5c518"/></svg></span><div><small>Address</small>418 Lakeview Commons Suite 210,<br>Riverton, MN 55990</div></div>
    <div class="contact-item"><span class="ic"><svg width="14" height="14" viewBox="0 0 14 14"><path d="M3 1.5h2.5l1 3-1.5 1a7 7 0 0 0 3.5 3.5l1-1.5 3 1V11a1.5 1.5 0 0 1-1.5 1.5A10 10 0 0 1 1.5 3 1.5 1.5 0 0 1 3 1.5z" fill="none" stroke="#f5c518" stroke-width="1.3"/></svg></span><div><small>Call Us</small>(555) 014-2286</div></div>
    <div class="contact-item"><span class="ic"><svg width="14" height="14" viewBox="0 0 14 14"><rect x="1.5" y="3" width="11" height="8" rx="1" fill="none" stroke="#f5c518" stroke-width="1.3"/><path d="M1.5 3.5 7 8l5.5-4.5" fill="none" stroke="#f5c518" stroke-width="1.3"/></svg></span><div><small>Email</small>info@norvalith.com</div></div>
  </div>
  <div class="f-bottom">©2023. All rights reserved.</div>
  <div class="chat"><svg width="20" height="20" viewBox="0 0 20 20"><path d="M3 4h14v9H8l-4 3v-3H3z" fill="#1b1f2a"/></svg></div>
</footer>

</body>
</html>
```